Bright Arrow Delivery Service Wordpress design

My client is a delivery service whose motto is "We go where the freight leads us." Their colors are red, white and blue. They use Voyalo vans and box vans - NO semi tractors. They like this Website design www.tovamu-sample.com, but I would like to see some designs that make them stand out. Attached is their new logo.

Target Market(s)

Businesses who use delivery services in town and anyone needing freight picked up or transported in the United States.

Industry/Entity Type

Delivery Service

Number of Pages Required

1 page

Font styles to use
Sans Serif

Colors
ec1f27
0455a3
ffffff

Requirements
Must have
• We need a Wordpress design with sliders that incorporates their new logo and the motto "WE GO WHERE THE FREIGHT LEADS US" Their corporate colors are red, white and blue. They only use voyalo vans and box vans.
Nice to have
• Please use your creativity to come up with a unique design for this delivery service.
Should not have
• NO SEMI TRACTOR TRAILERS

```html
<!DOCTYPE html>
<html lang="en">
<head>
<meta charset="utf-8">
<title>Bright Arrow Delivery Service</title>
<link rel="stylesheet" href="https://fonts.googleapis.com/css2?family=Russo+One&family=Open+Sans:wght@400;600;700&family=Arimo:wght@400;700&display=swap">
<style>
:root{
  --red:#ec1f27;
  --blue:#0455a3;
  --white:#ffffff;
  --ink:#1a1a1a;
  --btn:#222222;
  --light:#f4f4f4;
  --grey:#ececec;
  --foot:#232323;
  --foot-line:#3a3a3a;
  --foot-text:#9a9a9a;
}
*{margin:0;padding:0;box-sizing:border-box}
html,body{width:710px;height:1200px;overflow:hidden;background:var(--white)}
body{position:relative;font-family:"Open Sans",sans-serif;color:var(--ink)}
.abs{position:absolute}

/* header */
.site-header{position:absolute;left:0;top:0;width:710px;height:72px;background:var(--white)}
.brand{left:36px;top:22px;display:flex;align-items:center;gap:8px}
.brand-dot{width:14px;height:14px;border-radius:50%;background:var(--blue)}
.brand-name{font-family:"Russo One",sans-serif;font-size:17px;color:var(--red);letter-spacing:.5px}
.top-links{right:36px;top:9px;display:flex;align-items:center;gap:6px;font-size:9px;font-weight:700}
.track{color:var(--blue);font-size:9.5px;margin-right:4px}
.tag-btn{color:var(--white);padding:5px 6px;font-size:8px}
.tag-btn.dark{background:var(--btn)}
.tag-btn.blue{background:var(--blue)}
.social-dot{width:8px;height:8px;border-radius:50%;background:var(--blue);margin-left:4px}
.main-nav{right:36px;top:38px;display:flex;font-size:8.5px;font-weight:700;text-transform:uppercase}
.main-nav span{padding:6px 7px;color:var(--ink)}
.main-nav .active{background:var(--blue);color:var(--white);padding:6px 10px}

/* hero */
.hero{left:0;top:72px;width:710px;height:328px;background:#e9e9e9}
.hero-photo{left:350px;top:72px;width:360px;height:328px;background:linear-gradient(100deg,#e9e9e9 0%,#d9b7a6 30%,#c59a6b 60%,#8a7355 100%)}
.hero-title{left:36px;top:182px;width:307px;height:58px;background:var(--red);color:var(--white);font-family:"Russo One",sans-serif;font-size:18.5px;line-height:21px;padding:9px 10px}
.hero-sub{left:36px;top:251px;color:var(--blue);font-weight:700;font-size:14px}
.btn{background:var(--btn);color:var(--white);font-size:10px;display:flex;align-items:center;justify-content:center}
.hero-btn{left:36px;top:281px;width:88px;height:27px}

/* services */
.section-title{left:0;width:710px;top:440px;text-align:center;font-family:"Russo One",sans-serif;font-size:19px;letter-spacing:.5px}
.card{width:179px;height:157px;background:var(--light)}
.card-icon{width:68px;height:68px;border-radius:50%;border:1.5px solid var(--blue);background:var(--white);display:flex;align-items:center;justify-content:center}
.card-title{width:179px;text-align:center;font-family:"Russo One",sans-serif;font-size:12.5px;line-height:17px}
.card-band{width:180px;height:25px;background:var(--red);color:var(--white);font-size:9px;font-weight:700;display:flex;align-items:center;justify-content:center}
.card-more{width:98px;height:25px;color:var(--white);font-size:9px;display:flex;align-items:center;justify-content:center}
.card-more svg{position:absolute;left:0;top:0}
.card-more span{position:relative}

/* quality */
.quality{left:0;top:727px;width:710px;height:258px;background:var(--grey)}
.quality-photo{left:20px;top:750px;width:240px;height:225px;background:linear-gradient(160deg,#d8b789,#b88e5c 60%,#e6e6e6)}
.quality-title{right:35px;top:775px;font-family:"Russo One",sans-serif;font-size:25px;color:var(--red);letter-spacing:.5px}
.quality-sub{right:35px;top:806px;font-size:16px;letter-spacing:.5px}
.quality-copy{right:35px;top:848px;width:400px;text-align:right;font-size:7.5px;line-height:13px;color:#555}
.quality-btn{left:568px;top:912px;width:107px;height:26px;font-size:9px}

/* footer */
.footer{left:0;top:985px;width:710px;height:215px;background:var(--foot);font-family:"Arimo",sans-serif}
.foot-h{color:var(--white);font-size:12.5px;font-weight:700;top:1012px}
.foot-h::after{content:"";position:absolute;left:0;top:22px;width:38px;height:1px;background:var(--foot-line)}
.foot-text{color:var(--foot-text);font-size:7.5px;line-height:13px}
.contact-line{color:#ccc;font-size:7.5px;display:flex;align-items:center;gap:5px}
.explore{color:var(--white);font-size:7.5px;line-height:19.7px}
.sub-input{left:478px;top:1051px;width:162px;height:23px;background:var(--white)}
.sub-btn{left:640px;top:1051px;width:35px;height:23px;background:var(--red);display:flex;align-items:center;justify-content:center}
.foot-rule{left:478px;top:1107px;width:197px;height:1px;background:var(--foot-line)}
.social-link{color:var(--white);font-size:7.5px;display:flex;align-items:center;gap:6px}
.social-link i{width:5px;height:5px;border-radius:50%;background:#bbb;display:inline-block}
.copyright{left:0;top:1176px;width:710px;height:24px;border-top:1px solid #333;color:#bbb;font-size:7px;text-align:center;line-height:22px;font-family:"Arimo",sans-serif}
</style>
</head>
<body>

<header class="site-header">
  <div class="abs brand"><span class="brand-dot"></span><span class="brand-name">BRIGHT ARROW</span></div>
  <div class="abs top-links">
    <span class="track">TRACK N' TRACE</span>
    <span class="tag-btn dark">LOGIN</span>
    <span class="tag-btn blue">SIGNUP</span>
    <span class="social-dot"></span><span class="social-dot"></span>
  </div>
  <nav class="abs main-nav">
    <span class="active">Home</span><span>Courier</span><span>Freight</span><span>About Us</span><span>Contact Us</span><span>Customer</span><span>Login</span>
  </nav>
</header>

<section>
  <div class="abs hero"></div>
  <div class="abs hero-photo" role="img" aria-label="Smiling courier holding a cardboard parcel in front of a red delivery van"></div>
  <h1 class="abs hero-title">WE GO WHERE THE FREIGHT LEADS US</h1>
  <p class="abs hero-sub">FAST AND CONVENIENT WAY OF DELIVERING</p>
  <div class="abs btn hero-btn">READ MORE</div>
</section>

<section>
  <h2 class="abs section-title">CHOOSE A SERVICE DIVISION</h2>

  <div class="abs card" style="left:36px;top:524px"></div>
  <div class="abs card-icon" style="left:89px;top:495px">
    <svg width="48" height="30" viewBox="0 0 48 30"><rect x="12" y="2" width="10" height="6" fill="#0455a3"/><rect x="4" y="9" width="26" height="13" fill="#0455a3"/><path d="M31 11h8l5 6v5H31z" fill="#0455a3"/><circle cx="12" cy="24" r="4" fill="#0455a3" stroke="#fff" stroke-width="1.5"/><circle cx="36" cy="24" r="4" fill="#0455a3" stroke="#fff" stroke-width="1.5"/></svg>
  </div>
  <h3 class="abs card-title" style="left:36px;top:575px">BRIGHT ARROW<br>EXPRESS COURIER</h3>
  <div class="abs card-band" style="left:35px;top:623px">OVER 750 EMPLOYEES TO SERVE YOU</div>
  <div class="abs card-more" style="left:75px;top:650px"><svg width="98" height="25"><path d="M0 0h98l-9 25H9z" fill="#0455a3"/></svg><span>Read More</span></div>

  <div class="abs card" style="left:267px;top:523px"></div>
  <div class="abs card-icon" style="left:320px;top:494px">
    <svg width="32" height="30" viewBox="0 0 32 30"><rect x="11" y="2" width="10" height="6" fill="none" stroke="#0455a3" stroke-width="2"/><rect x="1" y="7" width="30" height="22" fill="#0455a3"/><path d="M14 11h4v5h5v4h-5v5h-4v-5H9v-4h5z" fill="#fff"/></svg>
  </div>
  <h3 class="abs card-title" style="left:267px;top:574px">BRIGHT ARROW<br>MEDICAL ADVANTAGE</h3>
  <div class="abs card-band" style="left:266px;top:622px">MEDICAL SERVICES AVAILABLE</div>
  <div class="abs card-more" style="left:306px;top:649px"><svg width="98" height="25"><path d="M0 0h98l-9 25H9z" fill="#0455a3"/></svg><span>Read More</span></div>

  <div class="abs card" style="left:495px;top:524px"></div>
  <div class="abs card-icon" style="left:550px;top:495px">
    <svg width="34" height="34" viewBox="0 0 34 34"><path d="M3 3h5l5 22h17" fill="none" stroke="#0455a3" stroke-width="2"/><rect x="13" y="7" width="15" height="15" fill="#0455a3" transform="rotate(-12 20 14)"/><circle cx="14" cy="29" r="3" fill="#0455a3"/><circle cx="27" cy="29" r="3" fill="#0455a3"/></svg>
  </div>
  <h3 class="abs card-title" style="left:495px;top:575px">BRIGHT ARROW<br>EXPRESS FREIGHT</h3>
  <div class="abs card-band" style="left:494px;top:623px">ALL OF YOUR SHIPPING NEEDS</div>
  <div class="abs card-more" style="left:534px;top:650px"><svg width="98" height="25"><path d="M0 0h98l-9 25H9z" fill="#0455a3"/></svg><span>Read More</span></div>
</section>

<section>
  <div class="abs quality"></div>
  <div class="abs quality-photo" role="img" aria-label="Stack of open and closed cardboard boxes"></div>
  <h2 class="abs quality-title">THE BEST CUSTOMER SERVICE</h2>
  <p class="abs quality-sub">AND OPERATIONAL EXCELLENCE</p>
  <p class="abs quality-copy">Lorem ipsum dolor sit amet conse ctetur adipisicing elit, sed do eiusmod tempor incididunt ut labore et dolore magnaaliqua. Ut enim ad minim veniam, quis nostrud exercitation ullamco laboris nisi ut aliquip ex ea commodo consequat.Duis aute irure dolor in reprehenderit in voluptate velit esse cillum dolore eu fugiat nulla pariatur.</p>
  <div class="abs btn quality-btn">MORE INFORMATION</div>
</section>

<footer>
  <div class="abs footer"></div>

  <h4 class="abs foot-h" style="left:35px">Contact Us</h4>
  <p class="abs foot-text" style="left:38px;top:1045px;width:200px">Ledgerly Plus is one of the world's Leading financial consulting films.</p>
  <div class="abs contact-line" style="left:38px;top:1082px"><svg width="6" height="8" viewBox="0 0 6 8"><path d="M3 0a3 3 0 0 1 3 3c0 2-3 5-3 5S0 5 0 3a3 3 0 0 1 3-3z" fill="#aaa"/></svg>27 Merrow Lane, Halbury, England.</div>
  <div class="abs contact-line" style="left:38px;top:1101px"><svg width="7" height="7" viewBox="0 0 7 7"><path d="M1 0l2 2-1 1 2 2 1-1 2 2-1 1C3 7 0 4 0 1z" fill="#aaa"/></svg>(555) 0142 7788</div>
  <div class="abs contact-line" style="left:38px;top:1120px"><svg width="8" height="6" viewBox="0 0 8 6"><rect width="8" height="6" fill="#aaa"/><path d="M0 0l4 3 4-3" fill="none" stroke="#232323"/></svg>info@quillmark-demo.com</div>
  <div class="abs contact-line" style="left:38px;top:1139px"><svg width="8" height="7" viewBox="0 0 8 7"><rect x=".5" y=".5" width="7" height="4.5" fill="none" stroke="#aaa"/><rect x="2" y="6" width="4" height="1" fill="#aaa"/></svg>www.quillmark-demo.com</div>

  <h4 class="abs foot-h" style="left:273px;top:1013px">Explore</h4>
  <div class="abs explore" style="left:274px;top:1042px">Home<br>Service<br>News<br>Bonds<br>Investments<br>Stocks</div>
  <div class="abs explore" style="left:353px;top:1042px">About Us<br>Testimonials<br>Contact Us<br>Commodities<br>Retirement<br>Trends</div>

  <h4 class="abs foot-h" style="left:479px">Subscribe</h4>
  <div class="abs sub-input"></div>
  <div class="abs sub-btn"><svg width="12" height="9" viewBox="0 0 12 9"><rect x=".5" y=".5" width="11" height="8" fill="none" stroke="#fff"/><path d="M.5 .5l5.5 4.5 5.5-4.5" fill="none" stroke="#fff"/></svg></div>
  <p class="abs foot-text" style="left:478px;top:1081px">Get Latest updates and offers.</p>
  <div class="abs foot-rule"></div>
  <div class="abs social-link" style="left:479px;top:1121px"><i></i>Friendspace</div>
  <div class="abs social-link" style="left:558px;top:1121px"><i></i>Circles Plus</div>
  <div class="abs social-link" style="left:479px;top:1142px"><i></i>Chirper</div>
  <div class="abs social-link" style="left:558px;top:1141px"><i></i>Linkwork</div>

  <div class="abs copyright">© 2016 Brightarrow Right Reserved.</div>
</footer>

</body>
</html>
```